Digital Marketing Online Shop Needs a Home Page Web Design

Here is some background on the new home page and the message we want to relay to people visiting our site.
The new site design will be very similar to the following sites
http://trellisoft.com/
https://quillhaven.com/
http://brightmarrow.io/
http://sketchotter.com/
http://clipharbor.com/
We are a small marketing agency of 3 and we have built up and impressive contact list of partners over the last 16 years to help our customers take their digital marketing to the next level.
The four core areas of products we will be promoting and selling through our online shop are the following :
Web design
Content marketing
Graphic design
Coaching
We operate our agency in a new way, not the old school way so our customers can receive on-demand marketing.
We plan to have an online shop so visitors can purchase some of our services, very similar to how Quill Haven and Sketch Otter offer their services.
In the end, we want the same call to action layout as Trellisoft, Quill Haven and Sketch Otter, however, since we are an agency we would like to blend in Bright Marrow's layout.
We want the customer to either contact us about our services or purchase one of the services from our shop.
We are trying to make the whole digital marketing experience more transactional like retail and not so traditional servicey. :-)
It is from our years of experience and finding the right partners that allows us to offer this type of solution to businesses in the Maritime Provinces (New Brunswick, Nova Scotia, Prince Edward Island, Canada).
Also, because we are offering more of an on-demand/self serve option and we have lower overhead, we hope to pass along great pricing to our customers for their marketing needs. We really want this offer to expand outside of our local market in Saint John, New Brunswick.
I would also like to have a call to action written for a hero image at the top of the page, like the Trellisoft site.
After that I would like the content to flow through similar to Quill Haven & Trellisoft. But mix in some of the agency like content you see with Clipharbor, Bright Marrow.
I have also included the first draft of the content for our home page.
Menu Items will be About, How We Work, Learn, Shop, Contact
Please let me know if you need anything else.
Target Market(s)
Small businesses, 1-10 person companies with up to 5 million in revenue. Mostly service companies, but some retail.
Industry/Entity Type
Marketing
Number of Pages Required
1 page

```html
<!DOCTYPE html>
<html lang="en">
<head>
<meta charset="utf-8">
<title>Northwake Studio — Home</title>
<link href="https://fonts.googleapis.com/css2?family=Roboto:wght@300;400;500;700&display=swap" rel="stylesheet">
<style>
:root{
  --blue:#1f74cc;
  --ink:#2b2b2b;
  --muted:#666;
  --line:#e4e4e4;
  --pale:#eef0f6;
  --footer:#2d303a;
  --footer-deep:#25272f;
  --white:#fff;
}
*{box-sizing:border-box;margin:0;padding:0}
html,body{width:793px;height:1200px;overflow:hidden;background:var(--white)}
body{font-family:'Roboto',Arial,sans-serif;color:var(--ink);position:relative}
.section{position:absolute;left:0;width:793px}
.rule{display:block;width:26px;height:1px;background:#bbb;margin:0 auto}
.section-title{font-weight:300;font-size:15px;text-align:center;margin-top:8px}

/* header */
.site-header{top:0;height:46px;border-bottom:1px solid var(--line)}
.brand{position:absolute;left:59px;top:12px;display:flex;align-items:center;gap:6px}
.brand-dot{width:22px;height:22px;border-radius:50%;background:var(--blue)}
.brand-name{font-size:14px;font-weight:400;color:var(--blue);line-height:1}
.main-nav{position:absolute;right:60px;top:10px;display:flex;align-items:center;gap:22px;font-size:9px}
.main-nav .btn-outline{border:1px solid #ccc;padding:8px 10px;margin-left:-1px}

/* hero */
.hero{top:46px;height:284px}
.hero-photo{position:absolute;inset:0;background:linear-gradient(100deg,#d9dde0 0%,#eef0ef 35%,#dfe4e8 60%,#b9c3cc 100%)}
.hero-copy{position:absolute;left:59px;top:105px}
.hero-lead{font-size:14px;font-weight:300}
.hero-title{font-size:20px;font-weight:700;margin-top:1px}
.hero-actions{display:flex;gap:4px;margin-top:12px}
.btn{display:inline-flex;align-items:center;justify-content:center;font-size:9px;height:26px;padding:0 10px}
.btn-white{background:var(--white);color:var(--ink)}
.btn-blue{background:var(--blue);color:var(--white)}
.dots{position:absolute;left:59px;top:260px;display:flex;gap:4px}
.dots i{width:4px;height:4px;border-radius:50%;background:#aaa}
.dots i:first-child{background:#222}

/* features */
.features{top:330px;height:141px;padding-top:26px}
.feature-row{display:flex;justify-content:space-between;margin:14px 59px 0}
.feature{width:200px;text-align:center;font-size:11.5px;color:#444}
.feature svg{display:block;margin:0 auto 8px;height:36px}

/* services */
.services{top:471px;height:229px;background:var(--blue);color:var(--white);padding-top:28px}
.services .rule{background:rgba(255,255,255,.6)}
.service-grid{display:flex;gap:2px;margin:14px 59px 0 60px}
.service-card{width:167px;height:98px;background:rgba(255,255,255,.06);text-align:center;padding-top:14px}
.service-card.raised{box-shadow:0 3px 8px rgba(0,0,0,.25);background:rgba(255,255,255,.09)}
.service-card h3{font-weight:300;font-size:12px;margin:5px 0 6px}
.service-card p{font-size:7px;line-height:13px;opacity:.95}
.view-btn{display:block;width:76px;margin:20px auto 0;border:1px solid rgba(255,255,255,.55);height:26px;line-height:26px;text-align:center;font-size:9px}

/* reviews */
.reviews{top:700px;height:198px;padding-top:27px}
.review-grid{display:flex;gap:12px;margin:16px 59px 0}
.review{width:217px;height:101px;border:1px solid var(--line);box-shadow:0 1px 3px rgba(0,0,0,.06);padding:9px 12px}
.reviewer{display:flex;align-items:center;gap:7px;font-size:8px}
.avatar{width:23px;height:23px;border-radius:50%;background:#cfd4da}
.review p{font-size:7.4px;line-height:13px;color:var(--muted);margin-top:6px}

/* partners */
.partners{top:898px;height:59px;border-top:1px solid var(--line);display:flex;justify-content:space-around;align-items:center;padding:0 70px}
.partner{display:flex;align-items:center;gap:5px;font-size:8px;color:#888}
.partner i{width:14px;height:14px;border-radius:50%;background:#c2c6cc}

/* cta */
.cta{top:957px;height:64px;background:var(--pale)}
.cta .rule{position:absolute;left:59px;top:21px;margin:0}
.cta h2{position:absolute;left:59px;top:26px;font-weight:300;font-size:15px}
.cta .btn{position:absolute;left:672px;top:19px;height:26px;padding:0 10px}

/* footer */
.site-footer{top:1021px;height:150px;background:var(--footer);color:var(--white)}
.footer-brand{position:absolute;left:59px;top:46px;display:flex;align-items:center;gap:6px}
.footer-brand .brand-dot{background:#9aa0a8}
.footer-brand .brand-name{color:#c9ccd1}
.footer-btn{position:absolute;left:59px;top:86px}
.footer-col{position:absolute;top:33px;font-size:7.5px;line-height:15px}
.footer-col h4{font-size:8.5px;font-weight:500;margin-bottom:5px}
.footer-col h4::after{content:"";display:block;width:13px;height:1px;background:var(--blue);margin-top:4px}
.footer-col .strong{font-weight:500}
.footer-col .link{color:#4a90e2}
.social li{list-style:none;display:flex;align-items:center;gap:6px;margin-bottom:2.5px}
.social i{width:5px;height:5px;background:#ddd}
.social .link i{background:#4a90e2}
.footer-bottom{top:1171px;height:29px;background:var(--footer-deep);color:var(--white);font-size:8px;display:flex;align-items:center;justify-content:space-between;padding:0 60px 0 59px}
.footer-bottom nav{display:flex;gap:10px}
</style>
</head>
<body>

<header class="section site-header">
  <div class="brand">
    <span class="brand-dot"></span>
    <span class="brand-name">northwake studio</span>
  </div>
  <nav class="main-nav">
    <span>About</span><span>How We Work</span><span>Learn</span><span>Shop</span>
    <span class="btn-outline">Contact</span>
  </nav>
</header>

<section class="section hero">
  <div class="hero-photo" role="img" aria-label="Bright office with a small team working together at desktop computers"></div>
  <div class="hero-copy">
    <p class="hero-lead">Want an online presence</p>
    <h1 class="hero-title">for your small business??</h1>
    <div class="hero-actions"><span class="btn btn-white">Shop</span><span class="btn btn-blue">Contact</span></div>
  </div>
  <div class="dots"><i></i><i></i><i></i></div>
</section>

<section class="section features">
  <span class="rule"></span>
  <h2 class="section-title">What we provide</h2>
  <div class="feature-row">
    <div class="feature">
      <svg viewBox="0 0 36 36" width="36"><circle cx="18" cy="18" r="16" fill="none" stroke="#aaa" stroke-width="1.3"/><path d="M10 18l6 6 11-13" fill="none" stroke="#aaa" stroke-width="1.6"/></svg>
      Vetted Copywriters
    </div>
    <div class="feature">
      <svg viewBox="0 0 36 36" width="36"><path d="M8 12a13 13 0 1 1-2 8" fill="none" stroke="#1f74cc" stroke-width="2.6"/><path d="M3 10l5 3 3-5" fill="none" stroke="#1f74cc" stroke-width="2.6"/><path d="M19 11v8l5 4" fill="none" stroke="#1f74cc" stroke-width="2.6"/></svg>
      On-Time Delivery
    </div>
    <div class="feature">
      <svg viewBox="0 0 36 36" width="36"><circle cx="18" cy="12" r="6.5" fill="none" stroke="#aaa" stroke-width="1.3"/><path d="M5 32v-3c0-5 5-7 13-7s13 2 13 7v3z" fill="none" stroke="#aaa" stroke-width="1.3"/></svg>
      Fully Managed
    </div>
  </div>
</section>

<section class="section services">
  <span class="rule"></span>
  <h2 class="section-title">Services we provide</h2>
  <div class="service-grid">
    <div class="service-card"><svg viewBox="0 0 22 18" width="21" height="17"><rect x="1" y="2" width="20" height="13" fill="none" stroke="#fff" stroke-width="1.3"/><path d="M7 11l9-9" stroke="#fff" stroke-width="1.5"/><path d="M1 16.5h20" stroke="#fff" stroke-width="1.3"/></svg><h3>Web Design</h3><p>Let’s be honest. Your website is the face<br>of your business in the modern world.</p></div>
    <div class="service-card raised"><svg viewBox="0 0 22 18" width="21" height="17"><rect x="1" y="2" width="20" height="13" fill="none" stroke="#fff" stroke-width="1.3"/><path d="M7 11l9-9" stroke="#fff" stroke-width="1.5"/><path d="M1 16.5h20" stroke="#fff" stroke-width="1.3"/></svg><h3>Web Design</h3><p>Let’s be honest. Your website is the face<br>of your business in the modern world.</p></div>
    <div class="service-card"><svg viewBox="0 0 22 18" width="21" height="17"><rect x="1" y="2" width="20" height="13" fill="none" stroke="#fff" stroke-width="1.3"/><path d="M7 11l9-9" stroke="#fff" stroke-width="1.5"/><path d="M1 16.5h20" stroke="#fff" stroke-width="1.3"/></svg><h3>Web Design</h3><p>Let’s be honest. Your website is the face<br>of your business in the modern world.</p></div>
    <div class="service-card"><svg viewBox="0 0 22 18" width="21" height="17"><rect x="1" y="2" width="20" height="13" fill="none" stroke="#fff" stroke-width="1.3"/><path d="M7 11l9-9" stroke="#fff" stroke-width="1.5"/><path d="M1 16.5h20" stroke="#fff" stroke-width="1.3"/></svg><h3>Web Design</h3><p>Let’s be honest. Your website is the face<br>of your business in the modern world.</p></div>
  </div>
  <span class="view-btn">View Services</span>
</section>

<section class="section reviews">
  <span class="rule"></span>
  <h2 class="section-title">Customer Reviews</h2>
  <div class="review-grid">
    <article class="review"><div class="reviewer"><span class="avatar" role="img" aria-label="Portrait of Alan Moss"></span>Alan Moss</div><p>“Nec pede justo fringilla vel aliquet nec vulputate eget arcu in enim justo rhoncus ut imperdiet a venenatis vitae lorem ipsum dolor is some duumy text used by desig-ners!”</p></article>
    <article class="review"><div class="reviewer"><span class="avatar" role="img" aria-label="Portrait of Jenna Stroud"></span>Jenna Stroud</div><p>“Nec pede justo fringilla vel aliquet nec vulputate eget arcu in enim justo rhoncus ut imperdiet a venenatis vitae lorem ipsum dolor is some duumy text used by desig-ners!”</p></article>
    <article class="review"><div class="reviewer"><span class="avatar" role="img" aria-label="Portrait of Sean Jolliffe"></span>Sean Jolliffe</div><p>“Nec pede justo fringilla vel aliquet nec vulputate eget arcu in enim justo rhoncus ut imperdiet a venenatis vitae lorem ipsum dolor is some duumy text used by desig-ners!”</p></article>
  </div>
</section>

<section class="section partners">
  <span class="partner"><i></i>Calmbay</span>
  <span class="partner"><i></i>Plainmark</span>
  <span class="partner"><i></i>Rivetra</span>
  <span class="partner"><i></i>Samplo</span>
  <span class="partner"><i></i>Emberloop</span>
</section>

<section class="section cta">
  <span class="rule"></span>
  <h2>Contact us and get started with us!</h2>
  <span class="btn btn-blue">Get Started</span>
</section>

<footer class="section site-footer">
  <div class="footer-brand">
    <span class="brand-dot"></span>
    <span class="brand-name">northwake studio</span>
  </div>
  <span class="btn btn-blue footer-btn">Contact us now</span>
  <div class="footer-col" style="left:270px">
    <h4>ADDRESS</h4>
    <div class="strong">&#9679; Northwake Studio</div>
    <div style="margin-top:3px">Some address line...</div>
    <div>some location information here,</div>
    <div>Country name.</div>
  </div>
  <div class="footer-col" style="left:455px">
    <h4>CONTACT:</h4>
    <div class="strong">&#9993; Email:</div>
    <div class="link">info@northwakestudio.com</div>
    <div class="strong" style="margin-top:8px">&#9742; Telephone:</div>
    <div>+1 506 555 0142</div>
  </div>
  <div class="footer-col" style="left:614px">
    <h4>FOLLOW US</h4>
    <ul class="social">
      <li><i></i>Friendwall</li>
      <li class="link"><i></i>Chirper</li>
      <li><i></i>Circlenet</li>
      <li><i></i>Snapframe</li>
    </ul>
  </div>
</footer>

<div class="section footer-bottom">
  <span>© Northwake Studio</span>
  <nav><span>Privacy Policy</span><span>◦</span><span>Terms &amp; Conditions</span></nav>
</div>

</body>
</html>
```